Steady Path Physical Therapy and Wellness brochure

We need a trifold brochure that would go out to physicians. I am marketing to them to get patient referrals. My business name is Steady Path Physical Therapy and Wellness, PC. We specialize in treating balance and dizziness and other neurological disorders as well as in providing general physical therapy services. We could use a logo of some sort on the brochure. Please go to steadypathpt-example.com and look at the about page. My business does seminars too, but I want this brochure geared to the physical therapy services we provide. The business card I attached has important information and the phone and fax number. My address is:
41827 Harbor Crest Way, Suite #214
Laguna Niguel, CA 92058
I would like information on my business, but please include my name also. I am the sole physical therapist of the practice, but want to give the impression I am not just a small operation. I need the brochure to have Steady Path Physical Therapy and Wellness as the title, but information on me as the owner. I attached the brochure for some ideas. This is the one for my seminars. I don't want the new one geared toward seminars or this busy. However, the brochure does have some idea, like the graphic of the inner ear and then some information on me.
Thanks,
Updates
Project Deadline Extended Reason: Oh my gosh, I thought my deadline was May 13 and wanted to extend it beyond that. Can you please clarify what my deadlne is?I am new to this. Most of the designers have done something a bit different that I originally wanted.Perhaps due to language differences, this happened. However, I am liking what they have done.Please extend my deadline. I am a sole business owner.Thanks, Carla Added Wednesday, May 4, 2016
Target Market(s)
Physicians and perhaps patients
Industry/Entity Type
Business
Font styles to use
Requirements
Must have
- My business name, my name, phone and fax, address, my picture, an about section. Not overly busy. I work with people with balance problems.
- Please state I accept Medicare Insurance. Below is on the about section.
- Doctor of Physical Therapy
- Board Certified Geriatric Specialist
- QNRM Certified for Parkinson's treatment
- Vestibular Specialist
Nice to have
- all the above. please look at my website "about section"
- It's maybe okay to mention I am a part-time University professor, but maybe not too much on this.
Should not have
- not to busy, I attached an example of a trifold brochure since it has information on me, but I don't want something this busy.

```html
<!DOCTYPE html>
<html lang="en">
<head>
<meta charset="utf-8">
<title>Steady Path Physical Therapy and Wellness – Practice Brochure</title>
<link href="https://fonts.googleapis.com/css2?family=Open+Sans:ital,wght@0,300;0,400;0,600;0,700;1,400;1,600&display=swap" rel="stylesheet">
<style>
  :root{
    --teal:#12adc1;
    --teal-deep:#0a97ab;
    --teal-light:#8fd3de;
    --sky:#cbe8ef;
    --ink:#4a4a4a;
    --ink-soft:#6b6b6b;
    --paper:#ffffff;
    --stage:#ebebeb;
  }
  *{box-sizing:border-box;margin:0;padding:0}
  html,body{width:1200px;height:1020px;overflow:hidden}
  body{background:var(--stage);font-family:"Open Sans",Arial,sans-serif;color:var(--ink);position:relative}
  .panel{position:absolute;top:56px;width:388px;height:908px;overflow:hidden;background:var(--paper);box-shadow:0 2px 10px rgba(0,0,0,.12)}
  .panel--about{left:14px}
  .panel--services{left:406px;background:linear-gradient(180deg,var(--teal) 0%,var(--teal-deep) 100%);color:#fff}
  .panel--practice{left:798px}

  .wave{position:absolute;left:0;width:100%;display:block}
  .wave--top{top:0;height:190px}
  .wave--bottom{bottom:0;height:150px}

  /* about panel */
  .portrait{position:absolute;top:120px;left:44px;width:128px;height:128px;border-radius:50%;border:4px solid #fff;
    background:radial-gradient(circle at 50% 40%,#c9b3a0 0%,#9e8a7a 55%,#5d5550 100%);box-shadow:0 1px 4px rgba(0,0,0,.25)}
  .section-heading{font-weight:300;color:var(--teal);font-size:21px;line-height:22px;letter-spacing:.3px}
  .section-heading::after{content:"";display:block;margin-top:6px;width:150px;height:1px;background:var(--teal-light)}
  .about{position:absolute;top:290px;left:36px;right:36px}
  .owner-name{margin-top:14px;font-size:13px;font-weight:600;color:var(--ink)}
  .credentials{list-style:none;margin-top:8px;font-size:10.4px;line-height:15px;color:var(--ink-soft)}
  .credentials li{padding-left:14px;position:relative}
  .credentials li::before{content:"";position:absolute;left:0;top:5px;width:6px;height:6px;border-radius:50%;background:var(--teal)}
  .bio{margin-top:12px;font-size:10.4px;line-height:14px;text-align:justify;color:var(--ink-soft)}

  /* services panel */
  .block{padding:28px 24px 0}
  .block + .block{padding-top:22px}
  .block-title{display:flex;align-items:center;gap:10px;font-size:11.5px;font-weight:600;letter-spacing:.5px;margin-bottom:10px}
  .block-title::before,.block-title::after{content:"";flex:1;height:1px;background:rgba(255,255,255,.75)}
  .lead{font-size:10.4px;line-height:14px;margin-bottom:10px}
  .tick-list{list-style:none;font-size:10.4px;line-height:14px;border-bottom:1px solid rgba(255,255,255,.75);padding-bottom:12px}
  .tick-list li{display:grid;grid-template-columns:16px 1fr;margin-bottom:5px}
  .tick-list svg{width:10px;height:10px;margin-top:2px}

  /* practice panel */
  .photo-strip{position:absolute;top:0;left:0;width:100%;height:118px;background:linear-gradient(90deg,#f3f3f1 0%,#e4ddd6 45%,#d7d2cf 70%,#eef1f3 100%)}
  .practice{position:absolute;top:134px;left:26px;right:26px;font-size:10.4px;line-height:14px;color:var(--ink-soft)}
  .practice-name{font-size:17px;line-height:21px;font-weight:600;color:var(--teal)}
  .practice-tag{margin-top:4px;font-style:italic;color:var(--teal)}
  .practice-intro{margin-top:10px;text-align:justify}
  .practice h3{margin-top:12px;font-size:11.6px;font-weight:600;font-style:italic;color:var(--teal)}
  .practice ul{list-style:none;margin-top:4px}
  .practice li{padding-left:8px;text-indent:-8px}
  .practice li::before{content:"• "}
  .medicare{margin-top:14px;padding:8px 10px;border:1px solid var(--teal-light);text-align:center;color:var(--teal);font-weight:600}
  .contact{margin-top:14px;font-style:normal}
  .contact p{display:grid;grid-template-columns:54px 1fr;margin-bottom:3px}
  .contact b{font-weight:600;color:var(--ink)}
  .contact .web{color:var(--teal);font-weight:700}
  .footer-name{position:absolute;bottom:34px;left:30px;right:30px;text-align:center;color:#fff;font-style:italic;font-size:11px;line-height:14px}
</style>
</head>
<body>

<section class="panel panel--about" aria-label="About the owner">
  <svg class="wave wave--top" viewBox="0 0 388 190" preserveAspectRatio="none" aria-hidden="true">
    <rect width="388" height="190" fill="#fff"/>
    <path d="M0 0 H388 V70 C300 52 200 58 120 92 C70 112 30 120 0 118 Z" fill="var(--teal)"/>
    <path d="M0 118 C30 120 70 112 120 92 C200 58 300 52 388 70 V120 C300 100 210 108 130 128 C80 140 35 150 0 150 Z" fill="var(--sky)"/>
  </svg>
  <div class="portrait" role="img" aria-label="Portrait photo of the owner, Carla"></div>
  <div class="about">
    <h1 class="section-heading">ABOUT<br>YOUR THERAPIST</h1>
    <p class="owner-name">Carla Whitmore, PT, DPT</p>
    <ul class="credentials">
      <li>Doctor of Physical Therapy</li>
      <li>Board Certified Geriatric Specialist</li>
      <li>QNRM Certified for Parkinson's treatment</li>
      <li>Vestibular Specialist</li>
    </ul>
    <p class="bio">Carla founded Steady Path Physical Therapy and Wellness to give patients with dizziness, balance loss and neurological conditions focused, one-on-one care. Each visit is spent with a doctor of physical therapy who builds an evidence based plan around the goals of the patient and keeps the referring physician informed of progress. Carla also teaches part time at the university level, bringing current research straight into the clinic.</p>
  </div>
  <svg class="wave wave--bottom" viewBox="0 0 388 150" preserveAspectRatio="none" aria-hidden="true">
    <path d="M0 40 C120 70 260 60 388 30 V150 H0 Z" fill="var(--teal-light)"/>
    <path d="M0 60 C130 88 270 76 388 48 V150 H0 Z" fill="var(--teal)"/>
  </svg>
</section>

<section class="panel panel--services" aria-label="Services and conditions treated">
  <div class="block">
    <h2 class="block-title">WHY REFER TO US</h2>
    <p class="lead">Balance disorders may result from CVA, trauma, congenital disorders and numerous other conditions seen in all settings. Dizziness can cause vertigo, nausea, anxiety and fear of falling. Research has shown vestibular problems can be treated properly with balance rehabilitation.</p>
  </div>
  <div class="block">
    <h2 class="block-title">OUR SERVICES</h2>
    <ul class="tick-list">
      <li><svg viewBox="0 0 10 10" aria-hidden="true"><path d="M1 5 L4 8 L9 1" fill="none" stroke="#fff" stroke-width="1.6"/></svg><span>Vestibular and balance rehabilitation</span></li>
      <li><svg viewBox="0 0 10 10" aria-hidden="true"><path d="M1 5 L4 8 L9 1" fill="none" stroke="#fff" stroke-width="1.6"/></svg><span>BPPV testing and canalith repositioning</span></li>
      <li><svg viewBox="0 0 10 10" aria-hidden="true"><path d="M1 5 L4 8 L9 1" fill="none" stroke="#fff" stroke-width="1.6"/></svg><span>Fall risk assessment and prevention</span></li>
      <li><svg viewBox="0 0 10 10" aria-hidden="true"><path d="M1 5 L4 8 L9 1" fill="none" stroke="#fff" stroke-width="1.6"/></svg><span>Neurological rehabilitation</span></li>
      <li><svg viewBox="0 0 10 10" aria-hidden="true"><path d="M1 5 L4 8 L9 1" fill="none" stroke="#fff" stroke-width="1.6"/></svg><span>Parkinson's movement program</span></li>
      <li><svg viewBox="0 0 10 10" aria-hidden="true"><path d="M1 5 L4 8 L9 1" fill="none" stroke="#fff" stroke-width="1.6"/></svg><span>Gait and postural training</span></li>
      <li><svg viewBox="0 0 10 10" aria-hidden="true"><path d="M1 5 L4 8 L9 1" fill="none" stroke="#fff" stroke-width="1.6"/></svg><span>General orthopedic physical therapy</span></li>
    </ul>
  </div>
  <div class="block">
    <h2 class="block-title">CONDITIONS WE TREAT</h2>
    <ul class="tick-list">
      <li><svg viewBox="0 0 10 10" aria-hidden="true"><path d="M1 5 L4 8 L9 1" fill="none" stroke="#fff" stroke-width="1.6"/></svg><span>Dizziness, vertigo and imbalance</span></li>
      <li><svg viewBox="0 0 10 10" aria-hidden="true"><path d="M1 5 L4 8 L9 1" fill="none" stroke="#fff" stroke-width="1.6"/></svg><span>Vestibular neuritis, labyrinthitis, Meniere's</span></li>
      <li><svg viewBox="0 0 10 10" aria-hidden="true"><path d="M1 5 L4 8 L9 1" fill="none" stroke="#fff" stroke-width="1.6"/></svg><span>Stroke, concussion / TBI, MS</span></li>
      <li><svg viewBox="0 0 10 10" aria-hidden="true"><path d="M1 5 L4 8 L9 1" fill="none" stroke="#fff" stroke-width="1.6"/></svg><span>Parkinson's disease</span></li>
      <li><svg viewBox="0 0 10 10" aria-hidden="true"><path d="M1 5 L4 8 L9 1" fill="none" stroke="#fff" stroke-width="1.6"/></svg><span>Cervicogenic dizziness</span></li>
      <li><svg viewBox="0 0 10 10" aria-hidden="true"><path d="M1 5 L4 8 L9 1" fill="none" stroke="#fff" stroke-width="1.6"/></svg><span>Age related weakness and falls</span></li>
    </ul>
  </div>
</section>

<section class="panel panel--practice" aria-label="Practice and contact details">
  <div class="photo-strip" role="img" aria-label="Photo of a smiling older couple"></div>
  <div class="practice">
    <h2 class="practice-name">Steady Path Physical Therapy and Wellness</h2>
    <p class="practice-tag">Balance, dizziness and neurological care</p>
    <p class="practice-intro">We help patients regain confidence in everyday movement through thorough evaluation, hands-on treatment and clear home programs, with timely reports sent to every referring physician.</p>
    <h3>What patients can expect</h3>
    <ul>
      <li>Full one-hour visits with a doctor of physical therapy</li>
      <li>Evidence based, individualized treatment plans</li>
      <li>Measurable outcomes shared with your office</li>
      <li>Prompt scheduling for new referrals</li>
    </ul>
    <p class="medicare">We accept Medicare Insurance</p>
    <address class="contact">
      <p><b>Address</b><span>41827 Harbor Crest Way, Suite #214<br>Laguna Niguel, CA 92058</span></p>
      <p><b>Phone</b><span>(949) 555-0142</span></p>
      <p><b>Fax</b><span>(949) 555-0143</span></p>
      <p><b>Web</b><span class="web">www.steadypathpt-example.com</span></p>
    </address>
  </div>
  <svg class="wave wave--bottom" viewBox="0 0 388 150" preserveAspectRatio="none" aria-hidden="true">
    <path d="M0 34 C120 20 260 10 388 0 V150 H0 Z" fill="var(--teal-light)"/>
    <path d="M0 56 C130 36 270 24 388 18 V150 H0 Z" fill="var(--teal)"/>
  </svg>
  <p class="footer-name">Steady Path Physical Therapy and Wellness,<br>Professional Corporation</p>
</section>

</body>
</html>
```